Business card required for IT Consultancy Business - Tealbrook Consulting.
Company provides the whole nine yards of services across IT Architecture, design and execution.
Basically we provide consulting services to help businesses make sure their technology is enabling their business strategy.
Design for front and back required.
We would like the front of the card to inlcude:
Name
Title
Mobile number
email address
www.tbkc.com.au
Company logos attached.
Thank you
Industry/Entity Type
Business
Contact Information for Business Card
Name
Title
Mobile number
email address
www.tbkc.com.au
Look and feel
Each slider illustrates characteristics of the customer's brand and the style your logo design should communicate.

```html
<!DOCTYPE html>
<html lang="en">
<head>
<meta charset="utf-8">
<title>Tealbrook Consulting – Business Card</title>
<link rel="stylesheet" href="https://fonts.googleapis.com/css2?family=Lato:wght@400;700;900&display=swap">
<style>
  :root {
    --page-bg: #3a3a3c;
    --card-white: #ffffff;
    --card-black: #1c1c1e;
    --brand-blue: #1d74c4;
    --brand-orange: #ec5a24;
    --ink: #111111;
    --rule: #1a1a1a;
  }
  * { box-sizing: border-box; margin: 0; padding: 0; }
  html, body {
    width: 1200px; height: 900px; overflow: hidden;
    background: var(--page-bg);
    font-family: "Lato", Arial, sans-serif;
  }
  .canvas { position: relative; width: 1200px; height: 900px; }

  .card {
    position: absolute; width: 640px; height: 366px;
    border-radius: 2px;
    box-shadow: 0 18px 40px rgba(0,0,0,0.45);
  }

  /* Back of card */
  .card-back {
    left: 500px; top: 60px;
    background: var(--card-black);
    display: flex; align-items: center; justify-content: center;
  }
  .card-back .wordmark { font-size: 40px; }

  /* Front of card */
  .card-front {
    left: 60px; top: 474px;
    background: var(--card-white);
  }
  .wordmark {
    display: flex; align-items: center; gap: 12px;
    font-weight: 900; color: var(--brand-blue);
    letter-spacing: 0.5px; line-height: 1;
  }
  .wordmark-dot {
    width: 0.7em; height: 0.7em; border-radius: 50%;
    background: var(--brand-blue);
  }
  .card-front .wordmark {
    position: absolute; left: 40px; top: 40px; font-size: 30px;
  }
  .divider-top {
    position: absolute; left: 40px; right: 40px; top: 118px;
    border-top: 1.5px solid var(--rule);
  }
  .holder { position: absolute; left: 40px; top: 134px; }
  .holder-name {
    font-weight: 700; font-size: 21px; color: var(--ink);
    letter-spacing: 0.3px; text-transform: uppercase;
  }
  .holder-title {
    font-size: 12px; color: var(--brand-orange);
    text-transform: uppercase; letter-spacing: 0.4px; margin-top: 3px;
  }
  .contacts {
    position: absolute; right: 40px; bottom: 34px;
    border-top: 1.5px solid var(--rule);
    padding-top: 10px; width: 250px;
    display: flex; flex-direction: column; gap: 7px;
  }
  .contact-row {
    display: flex; align-items: center; justify-content: flex-end; gap: 10px;
    font-size: 16px; color: var(--ink);
  }
  .contact-icon {
    width: 22px; height: 22px; border-radius: 4px;
    background: var(--brand-orange);
    display: flex; align-items: center; justify-content: center;
    flex: none;
  }
  .contact-icon svg { width: 14px; height: 14px; }
</style>
</head>
<body>
<div class="canvas">

  <section class="card card-back" aria-label="Card back">
    <div class="wordmark"><span class="wordmark-dot"></span>Tealbrook Consulting</div>
  </section>

  <section class="card card-front" aria-label="Card front">
    <div class="wordmark"><span class="wordmark-dot"></span>Tealbrook Consulting</div>
    <div class="divider-top"></div>

    <div class="holder">
      <p class="holder-name">Daniel Harlow</p>
      <p class="holder-title">Managing Derector</p>
    </div>

    <div class="contacts">
      <div class="contact-row">
        <span>0400 000 000</span>
        <span class="contact-icon">
          <svg viewBox="0 0 14 14" fill="none" stroke="#fff" stroke-width="1.4">
            <rect x="3.5" y="1" width="7" height="12" rx="1.2"/>
            <line x1="6" y1="11" x2="8" y2="11"/>
          </svg>
        </span>
      </div>
      <div class="contact-row">
        <span>info@tbkc.com.au</span>
        <span class="contact-icon">
          <svg viewBox="0 0 14 14" fill="none" stroke="#fff" stroke-width="1.4">
            <rect x="1" y="3" width="12" height="8.5"/>
            <polyline points="1,3 7,8 13,3"/>
          </svg>
        </span>
      </div>
      <div class="contact-row">
        <span>www.tbkc.com.au</span>
        <span class="contact-icon">
          <svg viewBox="0 0 14 14" fill="none" stroke="#fff" stroke-width="1.2">
            <circle cx="7" cy="7" r="5.8"/>
            <ellipse cx="7" cy="7" rx="2.6" ry="5.8"/>
            <line x1="1.2" y1="7" x2="12.8" y2="7"/>
          </svg>
        </span>
      </div>
    </div>
  </section>

</div>
</body>
</html>
```